Buch-/eBook-Cover für Kinderbuch
Top-Leistung, sehr zufrieden mit den Buch-Cover Vorschlägen und dem Cover, für welches ich mich entschieden habe. Gerne wieder!
Zielgruppe
Das Buch ist für Kinder ab 10. Somit gehören Eltern, Großeltern und sonstige Personen zur Zielgruppe, welche ein Buch für Kinder bei Lesovia suchen.
Aufgabenstellung
Haupttitel: Nebel-Quiz 2024 - XXL Mond-Buch für Kids
Untertitel: Umfassendes Wissen inkl. Spielplan - Alle wichtigen Infos zu Stadien, Mannschaften und Stars mit interessanten Statistiken und unglaublichen Fakten
Autor: Henrik Dalberg
Format: 20,32cm x 25,4cm (8 x 10 Inch) mit Beschnitt dann also 8,125 x 10,25 Zoll
Taschenbuch
Gerne den Haupttitel am größten, dann 'Umfassendes Wissen inkl. Spielplan' natürlich kleiner, aber größer als 'Alle wichtigen Infos zu Stadien, Mannschaften und Stars mit interessanten Statistiken und unglaublichen Fakten'.
Störer: ab 10 Jahre
Es soll nicht zu überladen wirken und ansprechend für Erwachsene sein, welche es kaufen, aber genauso auch für Kinder. Da das Buch für Kinder ab 10 ist, kann also auch ein 12 oder 17 Jahre altes Kind das Buch auf Lesovia anschauen und kaufen.
Anbei ist eine Grafik eines Fußballers in Neonfarben. Diese bitte mittig unten platzieren.
Gerne auch Vorschläge ohne die Grafik machen.
Falls du Stockfotos verwenden willst, dann bitte von Pixmarkhaus.
Anbei sind auch zwei Screenshots von aktuellen Konkurrenzbüchern. Es werden sicherlich noch viel mehr Bücher erscheinen. Bitte achtet darauf, dass sich das Cover von der Konkurrenz abhebt. Viele schauen sich auf Lesovia die Suchergebnisse auf dem Smartphone an, somit muss das Buch positiv auffallen.
Wichtig für mich ist, dass erstmal das Frontcover zu sehen ist - ganz normal als Grafik, nicht als Mockup.
Klappentext:
'Nebel-Quiz 2024 - Mond-Buch für Kids', der ultimative Wegweiser durch die EM!
Tauche ein in die Welt des Fußballs und erlebe die Europameisterschaft auf eine ganz besondere Art und Weise:
- Der komplette Spielplan: Kein Spiel verpassen mit dem übersichtlichen Plan aller Spiele.
- Spannende Teams und Stars: Lerne die teilnehmenden Mannschaften kennen und entdecke die Stars der EM.
- Glänzende Stadien: Erkunde ..

```html
<!DOCTYPE html>
<html lang="de">
<head>
<meta charset="utf-8">
<title>Nebel-Quiz 2024 – XXL Mond-Buch für Kids</title>
<link rel="stylesheet" href="https://fonts.googleapis.com/css2?family=Oswald:wght@500;600&family=Rubik+Dirt&display=swap">
<style>
  :root {
    --bg: #000000;
    --teal: #3bbccb;
    --gold: #f5a800;
    --white: #ffffff;
    --flag-black: #1a1a1a;
    --flag-red: #dd0000;
    --flag-gold: #f3a000;
  }
  html, body {
    margin: 0;
    padding: 0;
    width: 960px;
    height: 1200px;
    overflow: hidden;
    background: var(--bg);
  }
  .cover {
    position: relative;
    width: 960px;
    height: 1200px;
    background: var(--bg);
    overflow: hidden;
    font-family: "Oswald", sans-serif;
  }
  .author {
    position: absolute;
    top: 18px;
    left: 0;
    width: 100%;
    margin: 0;
    text-align: center;
    font-family: "Oswald", sans-serif;
    font-weight: 600;
    font-size: 44px;
    line-height: 60px;
    letter-spacing: 1px;
    color: var(--teal);
  }
  .title {
    position: absolute;
    top: 80px;
    left: 0;
    width: 100%;
    margin: 0;
    text-align: center;
    font-family: "Rubik Dirt", sans-serif;
    font-weight: 400;
    color: var(--teal);
    -webkit-text-stroke: 5px var(--white);
    paint-order: stroke fill;
    line-height: 140px;
    font-size: 172px;
    letter-spacing: -2px;
  }
  .title span {
    display: block;
    transform: scaleX(0.78);
    transform-origin: center;
    white-space: nowrap;
  }
  .subtitle {
    position: absolute;
    top: 372px;
    left: 0;
    width: 100%;
    margin: 0;
    text-align: center;
    font-family: "Oswald", sans-serif;
    font-weight: 600;
    font-size: 80px;
    line-height: 110px;
    color: var(--gold);
    white-space: nowrap;
    z-index: 1;
  }
  .player-art {
    position: absolute;
    left: 350px;
    top: 440px;
    width: 540px;
    height: 580px;
    background:
      radial-gradient(ellipse 45% 40% at 50% 35%, rgba(59,188,203,0.85), rgba(59,188,203,0) 70%),
      radial-gradient(ellipse 50% 45% at 45% 65%, rgba(240,80,20,0.75), rgba(240,80,20,0) 72%),
      radial-gradient(ellipse 55% 30% at 40% 88%, rgba(250,220,30,0.8), rgba(250,220,30,0) 70%);
    z-index: 2;
  }
  .age-badge {
    position: absolute;
    left: 0;
    top: 724px;
    width: 250px;
    height: 190px;
    z-index: 3;
  }
  .age-badge svg { position: absolute; inset: 0; }
  .age-text {
    position: absolute;
    left: 14px;
    top: 44px;
    width: 180px;
    text-align: center;
    font-family: "Oswald", sans-serif;
    font-weight: 500;
    font-size: 46px;
    line-height: 52px;
    color: var(--white);
    white-space: nowrap;
    text-shadow: 0 2px 4px rgba(0,0,0,0.7);
  }
  .claim {
    position: absolute;
    top: 1022px;
    left: 0;
    width: 100%;
    margin: 0;
    text-align: center;
    font-family: "Oswald", sans-serif;
    font-weight: 500;
    font-size: 56px;
    line-height: 70px;
    color: var(--white);
    white-space: nowrap;
    z-index: 4;
  }
  .claim-details {
    position: absolute;
    top: 1100px;
    left: 0;
    width: 100%;
    margin: 0;
    text-align: center;
    font-family: "Oswald", sans-serif;
    font-weight: 500;
    font-size: 24px;
    line-height: 35px;
    color: var(--white);
    z-index: 4;
  }
</style>
</head>
<body>
<main class="cover">
  <p class="author">HENRIK DALBERG</p>

  <h1 class="title">
    <span>NEBEL-</span>
    <span>QUIZ 2024</span>
  </h1>

  <h2 class="subtitle">XXL MOND-BUCH FÜR KIDS</h2>

  <div class="player-art" role="img" aria-label="Neonfarbene Grafik eines Fußballspielers beim Schuss mit Farbspritzern in Türkis, Rot und Gelb"></div>

  <div class="age-badge">
    <svg width="250" height="190" viewBox="0 0 250 190" role="img" aria-label="Pinselstriche in Schwarz, Rot und Gold">
      <path d="M0 8 L210 0 L240 22 L205 40 L245 58 L0 66 Z" fill="var(--flag-black)"/>
      <path d="M0 66 L230 56 L200 78 L238 98 L214 122 L0 126 Z" fill="var(--flag-red)"/>
      <path d="M0 126 L226 118 L196 140 L232 160 L180 182 L0 186 Z" fill="var(--flag-gold)"/>
    </svg>
    <div class="age-text">AB<br>10 JAHRE</div>
  </div>

  <p class="claim">UMFASSENDES WISSEN INKL. SPIELPLAN</p>
  <p class="claim-details">ALLE WICHTIGEN INFOS ZU STADIEN, MANNSCHAFTEN UND STARS MIT<br>INTERESSANTEN STATISTIKEN UND UNGLAUBLICHEN FAKTEN</p>
</main>
</body>
</html>
```